Window Tinting Website Design

We are working with a Window Tinting company in California. They do commercial, residential, and automotive tint.

Some websites for inspiration:
https://www.velofilmz.com/
https://www.tkglossbay.com/
https://orbishadez.com/

Thank you for taking the time to consider designing a website for us. We are web developers based in Stockton, CA, USA. Most of our projects go through the same process. Understanding this process may help you win a project with us. We custom-code all of our websites in-house. We don’t have any requirements as to what tools you use for your design, but we ask that you follow these guidelines.

IMAGES:
If you use any images or icons in the design, we ask that you have a link to the asset so we can purchase the image/icon. Most of the designs we submit do not have the customer’s images on them unless they have some great images. Be creative; show us the feeling you are trying to portray with your image choices. Use any royalty-free site you choose. We subscribe to Brellix and mainly use their images, but we can purchase images outside of Brellix. PLEASE NOTE: we will not submit designs to clients with watermarks on the images.

FONTS:
We ask that you identify the fonts you’re using in the design. This can be done in a message if you want. We typically use Tarvo Fonts and Brellix Fonts.

CONTENT:
We're always open to different content and ideas. We often submit designs with stock images so the client can see our vision. We typically take pictures after the website launch to use their images with our vision. Lorem Ipsum is fine for paragraphs, but we ask that you make the Headers with correct English. We want to be able to show the vision and identify the sections of the website.

INSPIRATION:
We typically add a couple of links in the brief of websites we like to help you get started in your design.

REVISIONS:
We do not often ask for revisions of the designs unless we see something in the design that may not appeal to the client. If there are slight changes that we want to make, we do that in the development process.

FEEDBACK:
We rarely give feedback on designs during the design process. We are working on many website projects and do not have the time to provide feedback. We usually respond if your request is well thought out and asks specific questions, but a note asking “feedback, please” usually goes unanswered.

```html
<!DOCTYPE html>
<html lang="en">
<head>
<meta charset="utf-8">
<title>Nova Crest Window Tinting</title>
<link rel="stylesheet" href="https://fonts.googleapis.com/css2?family=Lato:ital,wght@0,400;0,700;0,900;1,700&display=swap">
<style>
  :root {
    --black: #000;
    --ink: #0a0a0a;
    --white: #fff;
    --blue: #6fa6d3;
    --btn: #5f9acb;
    --red: #c3001f;
    --red-line: #e5394f;
    --faint: #1c1c1c;
  }
  * { box-sizing: border-box; margin: 0; padding: 0; }
  html, body { width: 1200px; height: 2333px; overflow: hidden; }
  body { background: var(--black); color: var(--white); font-family: "Lato", sans-serif; position: relative; }
  .abs { position: absolute; }

  .hero { left: 0; top: 0; width: 1200px; height: 472px;
    background: linear-gradient(90deg, #050505 0%, #121212 35%, #3a2c0c 55%, #8a6a1c 78%, #a98522 100%); }
  .topbar { left: 0; top: 0; width: 1200px; height: 78px; background: rgba(20,20,20,.55); }
  .brand { display: flex; align-items: center; gap: 8px; font-weight: 900; font-size: 15px; color: var(--white); line-height: 1.1; }
  .brand .dot { width: 12px; height: 12px; border-radius: 50%; background: var(--red); flex: none; }
  .nav a { position: absolute; top: 26px; font-weight: 700; font-size: 20px; color: var(--white); text-decoration: none; }
  .nav-underline { left: 444px; top: 59px; width: 96px; height: 4px; background: var(--blue); }
  .btn { display: flex; align-items: center; justify-content: center; background: var(--btn); color: var(--white); font-weight: 900; text-decoration: none; }
  .contact-btn { left: 990px; top: 18px; width: 154px; height: 43px; font-size: 16px; }
  .rated-line { left: 56px; top: 180px; width: 112px; height: 5px; background: var(--white); }
  .rated { left: 180px; top: 165px; font-weight: 900; font-size: 29px; color: var(--blue); }
  .hero-title { left: 56px; top: 200px; font-weight: 900; font-size: 41px; line-height: 43px; }
  .quote-btn { left: 56px; top: 295px; width: 188px; height: 53px; font-size: 20px; }

  .why-title { left: 56px; top: 522px; font-weight: 900; font-size: 49px; }
  .why-sub { left: 56px; top: 578px; font-weight: 700; font-size: 19px; }
  .photo { display: block; }
  .num { font-weight: 900; font-size: 150px; line-height: 1; color: var(--faint); }
  .feature-title { font-weight: 900; font-size: 39px; line-height: 42px; color: var(--blue); }
  .feature-text { font-size: 27px; line-height: 39px; }

  .testimonial { left: 0; top: 1537px; width: 1200px; height: 443px; background: var(--ink); }
  .quote-text { left: 348px; top: 1603px; width: 660px; font-style: italic; font-weight: 700; font-size: 39px; line-height: 61px; }
  .author { left: 345px; top: 1860px; font-size: 22px; }

  .footer { left: 0; top: 1980px; width: 1200px; height: 353px; background: var(--red); }
  .footer-brand { left: 56px; top: 2110px; font-size: 34px; gap: 14px; }
  .footer-brand .dot { width: 26px; height: 26px; background: var(--white); }
  .footer-divider { left: 419px; top: 2072px; width: 3px; height: 170px; background: var(--red-line); }
  .footer-links a { position: absolute; font-weight: 900; font-size: 24px; color: var(--white); text-decoration: none; }
  .footer-rule { left: 56px; top: 2284px; width: 1088px; height: 3px; background: var(--red-line); }
  .copyright { left: 0; top: 2303px; width: 1200px; text-align: center; font-weight: 700; font-size: 11px; }
</style>
</head>
<body>
  <section class="hero abs" role="img" aria-label="Photo of a yellow car headlight and front bumper in low light"></section>
  <header>
    <div class="topbar abs"></div>
    <div class="brand abs" style="left:56px;top:20px;width:120px;"><span class="dot"></span><span>NOVA CREST<br>WINDOW TINTING</span></div>
    <nav class="nav">
      <a style="left:462px">HOME</a>
      <a style="left:556px">ABOUT</a>
      <a style="left:660px">TINTING</a>
    </nav>
    <div class="nav-underline abs"></div>
    <a class="btn contact-btn abs">CONTACT!</a>
  </header>

  <div class="rated-line abs"></div>
  <div class="rated abs">RATED #1</div>
  <h1 class="hero-title abs">Drive in the luxury of<br>a tinted car!</h1>
  <a class="btn quote-btn abs">GET A QUOTE!</a>

  <h2 class="why-title abs">Why choose us?</h2>
  <p class="why-sub abs">Our competive advantages will hook you!</p>

  <div class="photo abs" style="left:56px;top:670px;width:555px;height:370px;background:linear-gradient(180deg,#e6e7ec 0%,#b9bbc2 40%,#3b3c40 70%,#6d6e72 100%);" role="img" aria-label="Photo of a black sports sedan driving on a highway at dusk"></div>
  <div class="num abs" style="left:656px;top:635px;">1</div>
  <h3 class="feature-title abs" style="left:700px;top:672px;">CLEAN<br>CUSTOMIZATIONS</h3>
  <p class="feature-text abs" style="left:661px;top:790px;width:470px;">Our clean customizations will leave your car newer and fresher than the day before!</p>

  <div class="photo abs" style="left:659px;top:954px;width:487px;height:522px;background:linear-gradient(160deg,#8a7a66 0%,#5a4a3e 30%,#b3121c 55%,#6a0c12 80%,#3a3a3a 100%);" role="img" aria-label="Photo of a red hatchback parked among trees"></div>
  <div class="num abs" style="left:52px;top:1078px;">2</div>
  <h3 class="feature-title abs" style="left:102px;top:1112px;">QUALITY<br>SERVICES</h3>
  <p class="feature-text abs" style="left:63px;top:1232px;width:450px;">Whatever you need, we’ll do it, in fashion. We focus on providing our clients with quality tintings that’ll leave a mark in your life!</p>

  <section class="testimonial abs"></section>
  <svg class="abs" style="left:200px;top:1615px" width="115" height="102" viewBox="0 0 115 102" aria-hidden="true">
    <path d="M12 0h36L30 70c-4 18-10 30-22 30C0 100-2 88 2 74Z" fill="var(--red)"/>
    <path d="M74 0h36L92 70c-4 18-10 30-22 30-8 0-10-12-6-26Z" fill="var(--red)"/>
  </svg>
  <blockquote class="quote-text abs">This business has took my car, turned it around into a beautifully tinted car. I’ve showed it around with my relatives and they’ve all liked it!</blockquote>
  <p class="author abs">- Darren</p>

  <footer>
    <div class="footer abs"></div>
    <div class="brand footer-brand abs"><span class="dot"></span><span>NOVA CREST<br>WINDOW TINTING</span></div>
    <div class="footer-divider abs"></div>
    <nav class="footer-links">
      <a style="left:445px;top:2085px">HOME</a>
      <a style="left:445px;top:2124px">ABOUT</a>
      <a style="left:445px;top:2163px">TINTING</a>
      <a style="left:445px;top:2202px">CONTACT US</a>
      <a style="left:673px;top:2085px">CHIRPLINE</a>
      <a style="left:673px;top:2124px">WORKRISE</a>
      <a style="left:673px;top:2163px">FRIENDSY</a>
      <a style="left:673px;top:2202px">SNAPFRAME</a>
    </nav>
    <div class="footer-rule abs"></div>
    <p class="copyright abs">Copyright ©2023 Nova Crest window tinting</p>
  </footer>
</body>
</html>
```